Kessler MD Summit Primary Care Business Card

Need a business card for a medical clinic targeting VIP patients. Should portray an upscale feeling. Simple, clean design. Logo and colors need to be incorporated into card. Clinic colors are gray/ silver, blues, white same as logo.
Clinic is a cash only VIP service clinic targeting higher income patients.
Tagline: "Where everyone is a VIP - Very Important Patient"

Target Market(s)

VIP, upscale

Industry/Entity Type

Medical

Contact Information for Business Card

Would like to use for cards with raised print or metallic highlight.

Requirements
Must have
• Incorporate logo, Use colors in logo
Nice to have
• Metallic detail
Should not have
• too much details or colors, other stock photos or designs

```html
<!DOCTYPE html>
<html lang="en">
<head>
<meta charset="utf-8">
<title>Kessler MD Summit Primary Care – Business Card</title>
<link rel="stylesheet" href="https://fonts.googleapis.com/css2?family=Cinzel:wght@400;600&display=swap">
<style>
  :root {
    --backdrop: #e9e9e7;
    --card: #ffffff;
    --navy: #2b3d55;
    --ink: #4a4d52;
    --silver: #9ea4ab;
  }
  * { margin: 0; padding: 0; box-sizing: border-box; }
  html, body {
    width: 1200px; height: 800px; overflow: hidden;
    background: var(--backdrop);
  }
  .card {
    position: absolute; left: 75px; top: 100px;
    width: 1050px; height: 600px;
    background: var(--card);
    box-shadow: 0 2px 10px rgba(0,0,0,0.08);
    font-family: "Cinzel", "Times New Roman", serif;
    color: var(--ink);
  }
  .card-frame { position: absolute; inset: 0; }
  .brand {
    position: absolute; left: 110px; top: 160px; width: 340px;
    text-align: center; color: var(--navy);
    font-weight: 600;
  }
  .brand-dot {
    width: 74px; height: 74px; border-radius: 50%;
    background: var(--silver);
    margin: 0 auto 26px;
  }
  .brand-name { font-size: 28px; line-height: 1.3; letter-spacing: 0.5px; }
  .contact {
    position: absolute; left: 560px; top: 165px;
    font-size: 20px; line-height: 30px;
  }
  .contact-name {
    font-size: 38px; font-weight: 600; color: var(--navy);
    margin-bottom: 18px; letter-spacing: 0.5px;
  }
  .contact-block { margin-bottom: 18px; }
  .tagline {
    position: absolute; left: 112px; top: 492px;
    font-size: 22px; color: var(--navy); letter-spacing: 0.4px;
  }
</style>
</head>
<body>
  <div class="card">
    <svg class="card-frame" width="1050" height="600" viewBox="0 0 1050 600" aria-hidden="true">
      <rect x="24" y="24" width="1002" height="552" fill="none" stroke="var(--navy)" stroke-width="2.5"/>
      <path d="M926 24 L1026 24 L1026 124 A100 100 0 0 0 926 24 Z" fill="var(--navy)"/>
      <path d="M24 476 L24 576 L124 576 A100 100 0 0 0 24 476 Z" fill="var(--navy)"/>
    </svg>

    <div class="brand">
      <div class="brand-dot"></div>
      <div class="brand-name">Kessler MD<br>Summit Primary Care</div>
    </div>

    <div class="contact">
      <div class="contact-name">Kessler Md</div>
      <div class="contact-block">PO Box 456 Fairhaven<br>NY 12345</div>
      <div>555-210-4830<br>care@kesslermd.com<br>www.kesslermd.com</div>
    </div>

    <div class="tagline">Where everyone is a VIP - Very Important Patient</div>
  </div>
</body>
</html>
```